Business Card for Jewelry Business

We need a new namecard design for a jewelry company based in Bangkok, Thailand. We have a new website recently and want the new namecard to reflect our new modern image. I have uploaded our old namecard to show you the information that needs to be on the namecard. Pls check our website www.qelburn.com for the new color scheme to help design the new namecard.

```html
<!DOCTYPE html>
<html lang="en">
<head>
<meta charset="utf-8">
<title>Qelburn Jewelry – Business Card</title>
<link rel="stylesheet" href="https://fonts.googleapis.com/css2?family=Jost:wght@400;500&display=swap">
<style>
  :root {
    --backdrop: #ababab;
    --card-white: #ffffff;
    --brand-teal: #5acdd2;
    --ring-beige: #ddd5c9;
    --ink-light: #ffffff;
  }
  * { margin: 0; padding: 0; box-sizing: border-box; }
  html, body { width: 1200px; height: 1000px; overflow: hidden; }
  body {
    background: var(--backdrop);
    font-family: "Jost", "Futura", sans-serif;
    position: relative;
  }
  .card {
    position: absolute;
    left: 294px;
    width: 613px;
    height: 352px;
    border-radius: 24px;
    text-align: center;
  }
  .card-front { top: 82px; background: var(--card-white); }
  .card-back { top: 545px; background: var(--brand-teal); color: var(--ink-light); }

  .brand-ring {
    position: absolute;
    left: 194px; top: 52px;
    width: 226px; height: 226px;
    border: 1.5px solid var(--ring-beige);
    border-radius: 50%;
    display: flex; align-items: center; justify-content: center;
  }
  .brand-ring .brand-name {
    font-size: 30px; font-weight: 400; letter-spacing: 2px;
    color: var(--brand-teal);
  }
  .website {
    position: absolute; left: 0; right: 0; top: 301px;
    font-size: 20px; letter-spacing: 2.5px;
    color: var(--brand-teal);
  }

  .back-brand {
    position: absolute; left: 0; right: 0; top: 48px;
    font-size: 20px; font-weight: 400; letter-spacing: 0.5px;
  }
  .person-name {
    position: absolute; left: 0; right: 0; top: 134px;
    font-size: 44px; font-weight: 400; letter-spacing: 8px;
    line-height: 1;
  }
  .person-title {
    position: absolute; left: 0; right: 0; top: 189px;
    font-size: 14px; letter-spacing: 3.2px;
  }
  .contact-row {
    position: absolute; left: 0; right: 0; top: 239px;
    display: flex; justify-content: center; gap: 26px;
    font-size: 19px;
  }
  .contact-item { display: flex; align-items: center; gap: 5px; }
  .contact-item svg { width: 22px; height: 20px; }
  .address {
    position: absolute; left: 0; right: 0; top: 290px;
    font-size: 14.5px; line-height: 1.45;
  }
</style>
</head>
<body>
  <section class="card card-front">
    <div class="brand-ring"><span class="brand-name">Qelburn</span></div>
    <p class="website">www.qelburn.com</p>
  </section>

  <section class="card card-back">
    <p class="back-brand">Qelburn Jewelry</p>
    <h1 class="person-name">NALIN SAKDAPONG</h1>
    <p class="person-title">SALES &amp; PRODUCT DEVELOPMENT MANAGER</p>
    <div class="contact-row">
      <span class="contact-item">
        <svg viewBox="0 0 22 20" fill="none" stroke="#fff" stroke-width="1.6" stroke-linejoin="round">
          <path d="M5 2 L8 6 L6.5 8 Q8.5 12 12 14 L14 12.5 L18 15.5 L16 18 Q8 17 3 7 Z"/>
        </svg>+662-418-7730
      </span>
      <span class="contact-item">
        <svg viewBox="0 0 22 20" fill="none" stroke="#fff" stroke-width="1.6" stroke-linejoin="round">
          <rect x="1" y="3" width="20" height="14"/>
          <path d="M1 3 L11 11 L21 3 M1 17 L8 9 M21 17 L14 9"/>
        </svg>nalin@qelburn.com
      </span>
    </div>
    <p class="address">212 Moo 7 Srinakarin Road, Bang Na Industrial Park,<br>Bangkok, 10260 Thailand</p>
  </section>
</body>
</html>
```